Launch of Kolvaro.com

Need a banner ad for the launch of a new website that covers Singapore, Australia and India. The website is www.kolvaro.example (the Singapore one is www.kolvaro.example.sg and the India one is www.kolvaro.example.in). Note that all three are english speaking countries and the ad need to be in english.

The value proposition are :

a. It has all job listings available in the country and many times larger the nearest competitor job listing.
b. You can find almost any job you want in the country, kinda of infinite choices for you.
c. It is the coolest and hippest jobs search site.
(Avoid green and orange as they are the competitors' colors)
Updates

Project Deadline Extended
Reason: Some of the designs have come in pretty good, but need some touch up. I have given the feedback and appreciate the need to time to change.

Project Deadline Extended
Reason: I realised that the tagline that I guided you looks and sounds awful. I am making some changes and will revert to you. Sorry.

Target Market(s)

Mass market

Requirements
Must have
• Be daring in the statement, be bold in trying out use of pictures or graphics that is controversial or suggestive, as long it is not porn.
Should not have
• Premium look, or appeal only to the professional .

```html
<!DOCTYPE html>
<html lang="en">
<head>
<meta charset="utf-8">
<title>Kolvaro.com – Launch Banners</title>
<link href="https://fonts.googleapis.com/css2?family=Roboto+Condensed:wght@400;700&display=swap" rel="stylesheet">
<style>
  :root {
    --bg-light: #c4c4c4;
    --bg-dark: #8e8e8e;
    --red: #c62220;
    --red-deep: #9e1619;
    --red-bright: #e0332c;
    --ink: #111111;
    --white: #ffffff;
    --brand-blue: #2a9be0;
    --muted: #6b6b6b;
  }
  * { box-sizing: border-box; margin: 0; padding: 0; }
  html, body { width: 1200px; height: 979px; overflow: hidden; }
  body {
    position: relative;
    background: linear-gradient(180deg, var(--bg-light) 0%, var(--bg-dark) 100%);
    font-family: "Roboto Condensed", "Arial Narrow", sans-serif;
  }
  .banner { position: absolute; overflow: hidden; background: var(--red); }
  .banner svg.art { position: absolute; inset: 0; width: 100%; height: 100%; }
  .banner-skyscraper { left: 167px; top: 25px; width: 204px; height: 765px; }
  .banner-square { left: 397px; top: 426px; width: 383px; height: 318px; }
  .banner-leaderboard { left: 167px; top: 802px; width: 969px; height: 153px; }

  .copy { position: absolute; color: var(--white); text-align: center; font-weight: 700; }
  .headline { font-size: 46px; line-height: 1; letter-spacing: 0.5px; }
  .body-copy { font-weight: 400; font-size: 31px; line-height: 46px; }

  .sky-headline { left: 0; width: 100%; top: 312px; }
  .sky-body { left: 0; width: 100%; top: 373px; }

  .square-headline { left: 0; width: 100%; top: 245px; font-size: 47px; }

  .board-headline { left: 210px; width: 550px; top: 14px; font-size: 50px; }
  .board-body { left: 210px; width: 550px; top: 70px; font-size: 25px; line-height: 34px; font-weight: 400; }

  .brand { position: absolute; text-align: right; line-height: 1; }
  .brand-name { display: block; font-family: "Roboto Condensed", "Arial Narrow", sans-serif; font-weight: 400; font-size: 34px; color: var(--brand-blue); }
  .brand-region { display: flex; align-items: center; justify-content: flex-end; gap: 4px; font-size: 11px; color: var(--white); margin-top: 1px; }
  .brand-region::before { content: ""; width: 9px; height: 6px; background: var(--white); }
  .sky-brand { right: 22px; top: 690px; }
  .square-brand { right: 28px; top: 176px; }
  .board-brand { right: 22px; top: 96px; }
</style>
</head>
<body>

  <!-- Skyscraper -->
  <section class="banner banner-skyscraper">
    <svg class="art" viewBox="0 0 204 765" preserveAspectRatio="none">
      <defs>
        <linearGradient id="skyPhoto" x1="0" y1="0" x2="1" y2="1">
          <stop offset="0" stop-color="#f2f2f2"/>
          <stop offset="1" stop-color="#9a9a9a"/>
        </linearGradient>
      </defs>
      <path d="M0 250 Q90 300 204 250 L204 300 Q100 330 0 290Z" fill="var(--red-deep)"/>
      <path d="M0 200 L204 110 L204 150 L150 285 L0 285Z" fill="var(--red-bright)"/>
      <polygon points="0,0 204,0 204,125 132,272 0,272" fill="var(--ink)"/>
      <polygon points="0,0 204,0 204,115 125,262 0,262" fill="var(--white)"/>
      <rect x="6" y="8" width="176" height="200" fill="url(#skyPhoto)" role="img" aria-label="Laptop showing job listings under a magnifying glass"/>
    </svg>
    <div class="copy headline sky-headline">YOU CAN</div>
    <div class="copy body-copy sky-body">find almost<br>any job you<br>want in the<br>country, kinda<br>of infinite<br>choices<br>for you</div>
    <div class="brand sky-brand"><span class="brand-name">Kolvaro</span><span class="brand-region">Singapore</span></div>
  </section>

  <!-- Square -->
  <section class="banner banner-square">
    <svg class="art" viewBox="0 0 383 318" preserveAspectRatio="none">
      <defs>
        <linearGradient id="squarePhoto" x1="0" y1="0" x2="1" y2="1">
          <stop offset="0" stop-color="#f2f2f2"/>
          <stop offset="1" stop-color="#9a9a9a"/>
        </linearGradient>
      </defs>
      <path d="M280 0 L300 0 L383 70 L383 90Z" fill="var(--white)"/>
      <path d="M320 0 L335 0 L383 40 L383 55Z" fill="var(--white)"/>
      <path d="M0 230 Q200 150 383 200 L383 230 Q200 180 0 255Z" fill="var(--red-deep)"/>
      <polygon points="0,0 258,0 118,200 0,163" fill="var(--ink)"/>
      <polygon points="0,0 246,0 110,188 0,154" fill="var(--white)"/>
      <rect x="4" y="4" width="200" height="150" fill="url(#squarePhoto)" role="img" aria-label="Laptop showing job listings under a magnifying glass"/>
    </svg>
    <div class="brand square-brand"><span class="brand-name">Kolvaro</span><span class="brand-region">Singapore</span></div>
    <div class="copy headline square-headline">JOB WANTED !!</div>
  </section>

  <!-- Leaderboard -->
  <section class="banner banner-leaderboard">
    <svg class="art" viewBox="0 0 969 153" preserveAspectRatio="none">
      <defs>
        <linearGradient id="boardPhoto" x1="0" y1="0" x2="1" y2="1">
          <stop offset="0" stop-color="#f2f2f2"/>
          <stop offset="1" stop-color="#9a9a9a"/>
        </linearGradient>
      </defs>
      <path d="M860 0 L880 0 L969 95 L969 118Z" fill="var(--white)"/>
      <path d="M905 0 L922 0 L969 50 L969 68Z" fill="var(--white)"/>
      <path d="M240 153 Q600 60 969 153Z" fill="var(--red-deep)" opacity="0.5"/>
      <polygon points="0,0 272,0 212,153 0,153" fill="var(--ink)"/>
      <polygon points="0,0 258,0 198,153 0,153" fill="var(--white)"/>
      <polygon points="0,128 90,153 0,153" fill="var(--red)"/>
      <rect x="30" y="4" width="170" height="130" fill="url(#boardPhoto)" role="img" aria-label="Laptop showing job listings under a magnifying glass"/>
    </svg>
    <div class="copy headline board-headline">JOB LISTINGS</div>
    <div class="copy board-body">available in the country and many times<br>larger the nearest competitor job listing</div>
    <div class="brand board-brand"><span class="brand-name">Kolvaro</span><span class="brand-region">Singapore</span></div>
  </section>

</body>
</html>
```